Brellow Gateworks garage door installation service and repairs

I need a business card design for my company that is called Brellow Gateworks, I install, service, repair and automate garaged doors.
I want my card to look simple and neat but I also want the information such as contact number, email address and website to be clear and noticeable. I would love a simple logo if possible, I would like to see the color blue in the card but not overpowering.

Industry/Entity Type

Garage

```html
<!DOCTYPE html>
<html lang="en">
<head>
<meta charset="utf-8">
<title>Brellow Gateworks – Business Card</title>
<link href="https://fonts.googleapis.com/css2?family=Montserrat:wght@400;500;700&display=swap" rel="stylesheet">
<style>
  :root {
    --brand-blue: #1f5aa6;
    --band-blue: #1a5aa8;
    --ink: #1c1c1c;
    --paper: #ffffff;
    --backdrop: #e9e9e9;
    --divider: #b9c6d8;
  }
  * { margin: 0; padding: 0; box-sizing: border-box; }
  html, body {
    width: 1200px;
    height: 1000px;
    overflow: hidden;
  }
  body {
    background: var(--backdrop);
    position: relative;
    font-family: "Montserrat", sans-serif;
    color: var(--ink);
  }
  .business-card {
    position: absolute;
    left: 246px;
    width: 704px;
    height: 420px;
    background: var(--paper);
    overflow: hidden;
  }
  .business-card.upper { top: 52px; }
  .business-card.lower { top: 526px; }

  .brand-block {
    position: absolute;
    top: 162px;
    left: 0;
    width: 100%;
    text-align: center;
  }
  .brand-name {
    font-size: 33px;
    font-weight: 700;
    color: var(--brand-blue);
    letter-spacing: 0.5px;
    text-transform: uppercase;
    line-height: 1;
  }
  .brand-tagline {
    margin-top: 8px;
    font-size: 13px;
    font-weight: 500;
    letter-spacing: 1px;
    color: var(--ink);
    text-transform: uppercase;
  }

  .holder {
    position: absolute;
    right: 374px;
    top: 318px;
    text-align: right;
  }
  .holder-name {
    font-size: 16px;
    font-weight: 700;
    color: var(--brand-blue);
    text-transform: uppercase;
    letter-spacing: 0.4px;
  }
  .holder-role {
    margin-top: 2px;
    font-size: 15px;
    font-weight: 500;
  }

  .divider {
    position: absolute;
    left: 351px;
    top: 298px;
    width: 1px;
    height: 78px;
    background: linear-gradient(to bottom, transparent, var(--divider) 20%, var(--divider) 80%, transparent);
  }

  .contact-list {
    position: absolute;
    left: 374px;
    top: 298px;
    list-style: none;
  }
  .contact-list li {
    display: flex;
    align-items: center;
    height: 18.5px;
    font-size: 15px;
    font-weight: 500;
  }
  .contact-list svg {
    width: 11px;
    height: 11px;
    margin-right: 9px;
    fill: var(--brand-blue);
    flex: none;
  }

  .footer-band {
    position: absolute;
    left: 0;
    bottom: 0;
    width: 100%;
    height: 29px;
    background: var(--band-blue);
  }
</style>
</head>
<body>

<section class="business-card upper">
  <div class="brand-block">
    <div class="brand-name">Brellow Gateworks</div>
    <div class="brand-tagline">Install | Repair | Automate Garaged Doors</div>
  </div>
  <div class="holder">
    <div class="holder-name">Tomas R. Hallwick</div>
    <div class="holder-role">Managing Director</div>
  </div>
  <div class="divider"></div>
  <ul class="contact-list">
    <li><svg viewBox="0 0 12 12"><path d="M3 1 L5 3.5 L4 4.8 C4.8 6.4 5.6 7.2 7.2 8 L8.5 7 L11 9 L9.8 11 C5.5 10.6 1.4 6.5 1 2.2 Z"/></svg>+ 999 999 9999</li>
    <li><svg viewBox="0 0 12 12"><rect x="3" y="0.5" width="6" height="3"/><rect x="0.5" y="4" width="11" height="5" rx="1"/><rect x="3" y="8" width="6" height="3.5"/></svg>+ 999 999 9999</li>
    <li><svg viewBox="0 0 12 12"><path d="M0.5 2 H11.5 V10 H0.5 Z M1.5 3 L6 6.5 L10.5 3" stroke="#fff" stroke-width="0.8"/></svg>info@brellowgateworks.com</li>
    <li><svg viewBox="0 0 12 12"><circle cx="6" cy="6" r="5.5"/><path d="M0.5 6 H11.5 M6 0.5 V11.5 M6 0.5 C3 3 3 9 6 11.5 M6 0.5 C9 3 9 9 6 11.5" stroke="#fff" stroke-width="0.7" fill="none"/></svg>www.brellowgateworks.com</li>
  </ul>
  <div class="footer-band"></div>
</section>

<section class="business-card lower">
  <div class="brand-block">
    <div class="brand-name">Brellow Gateworks</div>
    <div class="brand-tagline">Install | Repair | Automate Garaged Doors</div>
  </div>
  <div class="holder">
    <div class="holder-name">Tomas R. Hallwick</div>
    <div class="holder-role">Managing Director</div>
  </div>
  <div class="divider"></div>
  <ul class="contact-list">
    <li><svg viewBox="0 0 12 12"><path d="M3 1 L5 3.5 L4 4.8 C4.8 6.4 5.6 7.2 7.2 8 L8.5 7 L11 9 L9.8 11 C5.5 10.6 1.4 6.5 1 2.2 Z"/></svg>+ 999 999 9999</li>
    <li><svg viewBox="0 0 12 12"><rect x="3" y="0.5" width="6" height="3"/><rect x="0.5" y="4" width="11" height="5" rx="1"/><rect x="3" y="8" width="6" height="3.5"/></svg>+ 999 999 9999</li>
    <li><svg viewBox="0 0 12 12"><path d="M0.5 2 H11.5 V10 H0.5 Z M1.5 3 L6 6.5 L10.5 3" stroke="#fff" stroke-width="0.8"/></svg>info@brellowgateworks.com</li>
    <li><svg viewBox="0 0 12 12"><circle cx="6" cy="6" r="5.5"/><path d="M0.5 6 H11.5 M6 0.5 V11.5 M6 0.5 C3 3 3 9 6 11.5 M6 0.5 C9 3 9 9 6 11.5" stroke="#fff" stroke-width="0.7" fill="none"/></svg>www.brellowgateworks.com</li>
  </ul>
  <div class="footer-band"></div>
</section>

</body>
</html>
```